I LOVE BRAMBLE CREST

I would like a one page site that links to my real estate team website. Bramble Crest is a upscale and diverse subdivision in Bethesda Maryland about 30 minutes from downtown DC.
I am thinking of a modern Mayberry w/ a global-hip look.
We have T-Ball, Soccer, bike trails, bunnies, dogs and cats, bee-keepers, farmer markets, GREAT PUBLIC SCHOOLS
kids, kids, kids
I live in this area and love it and want to sell more houses here so I want this webpage to link to my site but be unique to this subdivision.

Target Market(s)

real estate - home sellers and home buyers

Industry/Entity Type

Real Estate Agent

Coding

Coded - Design and coding required

Number of Pages Required

1 page

Font styles to use
Sans Serif

Requirements
Must have
• Clear message The Orson & Mirela Team sells in Bramble Crest
Nice to have
• Images that reflect the fantastic Modern Mayberry meet hip Global world feel

```html
<!DOCTYPE html>
<html lang="en">
<head>
<meta charset="utf-8">
<title>I Love Bramble Crest</title>
<link rel="stylesheet" href="https://fonts.googleapis.com/css2?family=Montserrat:wght@400;600;700&family=Open+Sans:wght@400;600&display=swap">
<style>
:root{
  --brand:#9c1c3a;
  --brand-dark:#7c1530;
  --ink:#333;
  --muted:#8a8a8a;
  --line:#e3e3e3;
  --band:#f1f1f1;
  --footer:#2f2f2f;
  --footer-text:#bdbdbd;
}
*{box-sizing:border-box;margin:0;padding:0}
html,body{width:673px;height:1200px;overflow:hidden;background:#fff}
body{font-family:"Open Sans",Arial,sans-serif;color:var(--ink);font-size:6px;line-height:1.5;position:relative}

.site-header{height:58px;display:flex;align-items:center;justify-content:space-between;padding:0 56px}
.brand{display:flex;align-items:center;gap:7px}
.brand-mark{width:10px;height:10px;background:var(--brand)}
.brand-name{font-family:"Open Sans",Arial,sans-serif;font-weight:400;font-size:12px;color:var(--ink);letter-spacing:.2px}
.main-nav{display:flex;gap:13px;font-family:"Montserrat",Arial,sans-serif;font-size:6px;font-weight:600}
.main-nav a{color:var(--ink);text-decoration:none;padding-bottom:3px}
.main-nav a.active{color:var(--brand);border-bottom:1px solid var(--brand)}

.hero{position:relative;height:233px;background:linear-gradient(180deg,#cfdbe4 0%,#b8c8a4 35%,#8a6a52 55%,#6f7d4c 80%,#4f6b34 100%)}
.hero-caption{position:absolute;left:6px;top:98px;width:262px;height:108px;background:rgba(140,20,50,.88);color:#fff;padding:14px 16px}
.hero-caption h1{font-family:"Montserrat",Arial,sans-serif;font-size:13px;font-weight:700;margin-bottom:6px}
.hero-caption p{font-size:6px;line-height:1.6;color:#f1d9df}
.hero-caption a{display:inline-block;margin-top:6px;color:#fff;font-size:6px;font-weight:600}
.hero-arrow{position:absolute;top:100px;width:20px;height:20px;border-radius:50%;background:rgba(255,255,255,.35)}
.hero-arrow svg{display:block}
.hero-arrow.prev{left:10px}.hero-arrow.next{right:10px}

.strip{height:12px;background:var(--band)}
.intro{display:flex;gap:22px;padding:22px 56px 20px;border-bottom:1px solid var(--line);background:var(--band)}
.intro-item{flex:1;display:flex;flex-direction:column}
.intro-title{display:flex;align-items:center;gap:8px;font-family:"Montserrat",Arial,sans-serif;font-size:9px;font-weight:600;margin-bottom:8px;height:26px}
.intro-title .rule{flex:1;height:1px;background:#ccc}
.icon-circle{width:26px;height:26px;border-radius:50%;display:flex;align-items:center;justify-content:center}
.icon-circle.dark{background:#222}.icon-circle.red{background:var(--brand)}
.intro-item p{color:var(--muted)}

.content{display:flex;gap:24px;padding:20px 56px 0}
.sidebar{width:134px;flex:none}
.side-box{border:1px solid var(--line);margin-bottom:12px}
.side-box h3{background:var(--brand);color:#fff;font-family:"Montserrat",Arial,sans-serif;font-size:7.5px;font-weight:600;padding:5px 8px}
.side-box ul{list-style:none;padding:6px 8px}
.side-box li{display:flex;align-items:center;gap:5px;font-size:6px;color:#555;padding:2.5px 0}
.check{width:7px;height:7px;border:1px solid #999;flex:none}
.dot{width:4px;height:4px;border-radius:50%;background:#999;flex:none}

.main{flex:1}
.section-title{font-family:"Montserrat",Arial,sans-serif;font-weight:700;font-size:15px;text-align:center;margin-bottom:12px;color:#333}
.grid{display:flex;gap:14px;margin-bottom:42px}
.card{flex:1}
.card-media{height:84px;position:relative}
.price-tag{position:absolute;right:0;bottom:6px;background:var(--brand);color:#fff;font-size:5.5px;padding:2px 5px;font-weight:600}
.card-label{position:absolute;left:6px;top:34px;font-size:6px;color:#fff;background:rgba(0,0,0,.3);padding:1px 4px}
.card h4{font-family:"Montserrat",Arial,sans-serif;font-size:7px;font-weight:600;margin-top:6px}
.card .price{font-size:7px;font-weight:600;color:var(--brand);margin-bottom:3px}
.card p{color:var(--muted);margin-top:4px}
.card-listing{border:1px solid var(--line);padding:4px}
.card-listing p{margin-top:0}

.site-footer{position:absolute;left:0;top:1035px;width:673px;height:131px;background:var(--footer);color:var(--footer-text);display:flex;gap:24px;padding:18px 56px}
.footer-col{flex:1}
.footer-col h5{font-family:"Montserrat",Arial,sans-serif;color:#fff;font-size:8px;font-weight:600;margin-bottom:8px}
.footer-col ul{list-style:none}
.footer-col li{font-size:6px;padding:2px 0;display:flex;gap:5px;align-items:center}
.footer-col .dot{background:#777}
.bottom-bar{position:absolute;left:0;top:1166px;width:673px;height:34px;background:var(--brand-dark);color:#f0d7dd;display:flex;align-items:center;justify-content:space-between;padding:0 56px;font-size:6px}
.social{display:flex;gap:5px}
.social span{width:12px;height:12px;border-radius:50%;background:#fff;opacity:.85}
</style>
</head>
<body>
<header class="site-header">
  <div class="brand"><span class="brand-mark"></span><span class="brand-name">I Love Bramble Crest</span></div>
  <nav class="main-nav">
    <a class="active" href="#">HOME</a><a href="#">SEARCH</a><a href="#">SELLING</a><a href="#">BUYING</a><a href="#">ABOUT</a><a href="#">BLOG</a><a href="#">CONTACT</a>
  </nav>
</header>

<section class="hero" role="img" aria-label="Photo of a large brick colonial home with white columns, lawn and trees in Bramble Crest">
  <span class="hero-arrow prev"><svg width="20" height="20"><path d="M12 6 8 10l4 4" stroke="#fff" stroke-width="1.5" fill="none"/></svg></span>
  <span class="hero-arrow next"><svg width="20" height="20"><path d="M8 6l4 4-4 4" stroke="#fff" stroke-width="1.5" fill="none"/></svg></span>
  <div class="hero-caption">
    <h1>BETHESDA MARYLAND</h1>
    <p>Bramble Crest is an upscale and diverse subdivision in Bethesda, about thirty minutes from downtown DC, with great public schools, bike trails, farmer markets and friendly neighbors.</p>
    <a href="#">Read More »</a>
  </div>
</section>

<div class="strip"></div>
<section class="intro">
  <div class="intro-item">
    <div class="intro-title"><span>Welcome to I Love Bramble Crest</span><span class="rule"></span></div>
    <p>Lorem ipsum is simply dummy text of the printing and typesetting industry. Lorem ipsum has been the industry's standard dummy text ever since the 1500s.</p>
  </div>
  <div class="intro-item">
    <div class="intro-title"><span class="icon-circle dark"><svg width="12" height="12"><circle cx="5" cy="5" r="3.5" stroke="#fff" stroke-width="1.5" fill="none"/><path d="M7.6 7.6 11 11" stroke="#fff" stroke-width="1.6"/></svg></span><span>Search Listings</span><span class="rule"></span></div>
    <p>Lorem ipsum is simply dummy text of the printing and typesetting industry. Lorem ipsum has been the industry's standard dummy text ever since the 1500s.</p>
  </div>
  <div class="intro-item">
    <div class="intro-title"><span class="icon-circle red"><svg width="12" height="12"><rect x="1.5" y="2" width="9" height="6" rx="1" fill="#fff"/><path d="M3 8v3l3-3" fill="#fff"/></svg></span><span>Recent News</span><span class="rule"></span></div>
    <p>Lorem ipsum is simply dummy text of the printing and typesetting industry. Lorem ipsum has been the industry's standard dummy text ever since the 1500s.</p>
  </div>
</section>

<div class="content">
  <aside class="sidebar">
    <div class="side-box">
      <h3>Communities</h3>
      <ul>
        <li><span class="check"></span>All Communities</li>
        <li><span class="check"></span>District of Columbia NW</li>
        <li><span class="check"></span>District of Columbia NE</li>
        <li><span class="check"></span>District of Columbia SE</li>
        <li><span class="check"></span>District of Columbia SW</li>
        <li><span class="check"></span>Maryland</li>
        <li><span class="check"></span>Virginia</li>
      </ul>
    </div>
    <div class="side-box">
      <h3>Navigation</h3>
      <ul>
        <li><span class="dot"></span>Today's New Listings</li>
        <li><span class="dot"></span>Property Search</li>
        <li><span class="dot"></span>Map Search</li>
        <li><span class="dot"></span>Neighborhood Search</li>
        <li><span class="dot"></span>Condo Building Search</li>
        <li><span class="dot"></span>Luxury Search</li>
        <li><span class="dot"></span>About Us</li>
      </ul>
    </div>
  </aside>

  <main class="main">
    <h2 class="section-title">LISTINGS OF HOUSES</h2>
    <div class="grid">
      <article class="card card-listing">
        <div class="card-media" role="img" aria-label="Photo of a two-storey family house with a front lawn" style="background:linear-gradient(180deg,#bcd3e6,#8d9a6a 70%,#5e7a3a)"><span class="price-tag">Sale</span></div>
        <h4>Finibus Bonorum</h4><div class="price">For only $900.00</div>
        <p>Lorem ipsum is simply dummy text of the printing and typesetting industry. Lorem ipsum dolor sit amet.</p>
      </article>
      <article class="card card-listing">
        <div class="card-media" role="img" aria-label="Photo of a white suburban home with porch" style="background:linear-gradient(180deg,#c9dbe8,#d8d6cc 55%,#6f8a48)"><span class="price-tag">Sale</span></div>
        <h4>Finibus Bonorum</h4><div class="price">For only $900.00</div>
        <p>Lorem ipsum is simply dummy text of the printing and typesetting industry. Lorem ipsum dolor sit amet.</p>
      </article>
      <article class="card card-listing">
        <div class="card-media" role="img" aria-label="Photo of a brick house with trees" style="background:linear-gradient(180deg,#a9c4dc,#9a7058 55%,#587a36)"><span class="price-tag">Sale</span></div>
        <h4>Finibus Bonorum</h4><div class="price">For only $900.00</div>
        <p>Lorem ipsum is simply dummy text of the printing and typesetting industry. Lorem ipsum dolor sit amet.</p>
      </article>
    </div>

    <h2 class="section-title">FEATURED BRAMBLE CREST</h2>
    <div class="grid">
      <article class="card">
        <div class="card-media" role="img" aria-label="Photo of children playing together outdoors" style="background:linear-gradient(180deg,#e9c46a,#d98b3a 60%,#9c6a2e)"><span class="card-label">Happiness</span></div>
        <p>Lorem ipsum is simply dummy text of the printing and typesetting industry. Lorem ipsum dolor.</p>
      </article>
      <article class="card">
        <div class="card-media" role="img" aria-label="Photo of a family enjoying a sunny park" style="background:linear-gradient(180deg,#f2d27a,#c9a04a 55%,#8aa045)"><span class="card-label">Families</span></div>
        <p>Lorem ipsum is simply dummy text of the printing and typesetting industry. Lorem ipsum dolor.</p>
      </article>
      <article class="card">
        <div class="card-media" role="img" aria-label="Photo of fresh produce at a farmer market" style="background:linear-gradient(180deg,#c0392b,#e07b2e 50%,#6a8f2e)"><span class="card-label">Farmer Market</span></div>
        <p>Lorem ipsum is simply dummy text of the printing and typesetting industry. Lorem ipsum dolor.</p>
      </article>
    </div>

    <h2 class="section-title">FEATURE COMMUNITY</h2>
    <div class="grid">
      <article class="card">
        <div class="card-media" role="img" aria-label="Photo of a youth soccer game on a grass field" style="background:linear-gradient(180deg,#d7e6ef,#7fa84a 55%,#4f7a2a)"></div>
        <p>Lorem ipsum is simply dummy text of the printing and typesetting industry. Lorem ipsum dolor.</p>
      </article>
      <article class="card">
        <div class="card-media" role="img" aria-label="Photo of neighbors gathered at a community event" style="background:linear-gradient(180deg,#e8d9c4,#c98a5a 55%,#7a5a3a)"></div>
        <p>Lorem ipsum is simply dummy text of the printing and typesetting industry. Lorem ipsum dolor.</p>
      </article>
      <article class="card">
        <div class="card-media" role="img" aria-label="Photo of a bike trail through green woods" style="background:linear-gradient(180deg,#cfe0ea,#9cb8c8 45%,#5f8a4a)"></div>
        <p>Lorem ipsum is simply dummy text of the printing and typesetting industry. Lorem ipsum dolor.</p>
      </article>
    </div>
  </main>
</div>

<footer class="site-footer">
  <div class="footer-col"><h5>Most Viewed Pages</h5><ul>
    <li><span class="dot"></span>About Us</li><li><span class="dot"></span>Today's New Listings</li><li><span class="dot"></span>Search All Listings</li><li><span class="dot"></span>Find Your Home Value</li><li><span class="dot"></span>Mortgage Calculator</li></ul></div>
  <div class="footer-col"><h5>Buying</h5><ul>
    <li><span class="dot"></span>Home Finder</li><li><span class="dot"></span>Our Guarantee</li><li><span class="dot"></span>Mortgage Calculator</li><li><span class="dot"></span>First Time Buyers</li></ul></div>
  <div class="footer-col"><h5>Selling</h5><ul>
    <li><span class="dot"></span>About Us</li><li><span class="dot"></span>Contact</li><li><span class="dot"></span>Marketing Plan</li><li><span class="dot"></span>Home Evaluation</li></ul></div>
  <div class="footer-col"><h5>Get in contact</h5><ul>
    <li><span class="dot"></span>The Orson &amp; Mirela Team</li><li><span class="dot"></span>1 800 555 0142</li><li><span class="dot"></span>hello@bramblecrest.example</li><li><span class="dot"></span>48 Larkspur Lane, Bethesda MD</li></ul></div>
</footer>
<div class="bottom-bar">
  <span>© Copy Rights 2016, Bramble Crest Realty. Inc.</span>
  <span class="social"><span></span><span></span><span></span><span></span><span></span></span>
</div>
</body>
</html>
```